New profile page for existing party website

For the party website 'Revelmap' we need a new design for the user profile page.

The page should show
* a profile picture
* basic information like name, age and city
* music styles he/she likes
* links to their Chatterly profile and website
* a bio (HTML content)
* events they plan to go to
* past events
* pictures

Challenge is that some users may have little information (just their name) while others have a huge description, lots of foto's, events, etc.

Please visit http://www.revelmap.example and http://www.revelmap.example/users/gordon

Target Market(s)

Men and women between 18 and 35

Industry/Entity Type

Night Club

Number of Pages Required

2 page

Font styles to use
Other font styles liked:
• Roboto

Requirements
Must have
• Please design how the page looks with a fully filled out profile and with an empty profile.
• It should fit well with the existing website.
• Include designs for both for small screens (mobile) and large screens (tablet, desktop).
Nice to have
• UX design on how to collapse or paginate sections.
• Interactive effects would be a bonus.
Should not have
• The page should not have subnavigation like menus or tabs.

```html
<!DOCTYPE html>
<html lang="en">
<head>
<meta charset="utf-8">
<title>Gordon Hale – Revelmap profile</title>
<link href="https://fonts.googleapis.com/css2?family=Lato:wght@300;400&display=swap" rel="stylesheet">
<style>
  :root {
    --sidebar-bg: #2b2b2b;
    --sidebar-foot: #222222;
    --sidebar-text: #f2f2f2;
    --sidebar-muted: #bdbdbd;
    --sidebar-rule: #d8d8d8;
    --page-bg: #f8f8f8;
    --card-bg: #ffffff;
    --rule: #cfcfcf;
    --heading: #3a3a3a;
    --body-text: #2f2f2f;
  }
  * { box-sizing: border-box; margin: 0; padding: 0; }
  html, body { width: 1200px; height: 582px; overflow: hidden; }
  body {
    font-family: "Lato", sans-serif;
    background: var(--page-bg);
    position: relative;
  }

  /* Sidebar */
  .profile-sidebar {
    position: absolute; left: 0; top: 0;
    width: 187px; height: 582px;
    background: var(--sidebar-bg);
    color: var(--sidebar-text);
  }
  .profile-avatar {
    position: absolute; left: 47px; top: 22px;
    width: 94px; height: 94px; border-radius: 50%;
    background: radial-gradient(circle at 50% 45%, #8a5a3a 0%, #6b3f22 55%, #3a2414 100%);
  }
  .profile-name {
    position: absolute; left: 0; width: 187px; top: 129px;
    text-align: center; font-weight: 300; font-size: 22px;
  }
  .sidebar-rule {
    position: absolute; left: 8px; width: 172px; height: 1px;
    background: var(--sidebar-rule);
  }
  .sidebar-rule.top { top: 222px; }
  .sidebar-rule.bottom { top: 268px; }
  .section-label {
    position: absolute; left: 0; width: 187px; top: 237px;
    text-align: center; font-weight: 300; font-size: 13px;
    color: var(--sidebar-muted);
  }
  .video-thumb {
    position: absolute; left: 8px; top: 306px;
    width: 171px; height: 140px;
    background: linear-gradient(180deg, #8c93b6 0%, #5b6388 45%, #2a2c3c 100%);
  }
  .video-title {
    position: absolute; left: 6px; top: 5px;
    font-size: 7px; color: #ffffff;
  }
  .video-play {
    position: absolute; left: 80px; top: 63px;
  }
  .sidebar-footer {
    position: absolute; left: 0; bottom: 0;
    width: 187px; height: 33px;
    background: var(--sidebar-foot);
    display: flex; justify-content: space-around; align-items: center;
    font-size: 9px; color: #e6e6e6;
  }

  /* Main */
  .events {
    position: absolute; left: 187px; top: 0;
    width: 1013px; height: 582px; overflow: hidden;
  }
  .events-heading {
    position: absolute; left: 100px; width: 800px; top: 68px;
    text-align: center; font-weight: 300; font-size: 19px;
    color: var(--heading);
  }
  .events-rule {
    position: absolute; left: 100px; top: 104px;
    width: 800px; height: 1px; background: var(--rule);
  }
  .event-card {
    position: absolute; left: 100px; width: 800px; height: 114px;
    background: var(--card-bg);
    box-shadow: 0 1px 2px rgba(0,0,0,0.08);
    display: flex; align-items: flex-start;
  }
  .event-image { width: 183px; height: 114px; flex: none; }
  .event-text { padding-left: 38px; padding-top: 30px; }
  .event-title {
    font-weight: 300; font-size: 19px; line-height: 22px;
    color: var(--heading);
    margin-bottom: 5px;
  }
  .event-desc { font-size: 12px; line-height: 15px; color: var(--body-text); }
  .img-sunset { background: linear-gradient(180deg, #4a6a6a 0%, #c9b46a 60%, #2a2a22 100%); }
  .img-meadow { background: linear-gradient(180deg, #c8ccd2 0%, #9aa8a0 45%, #4f8a2a 70%, #3f6a20 100%); }
  .img-balloons { background: linear-gradient(135deg, #e9e8c4 0%, #a8d8c8 45%, #3a6f7a 100%); }
  .img-aviator { background: linear-gradient(180deg, #6b5a4c 0%, #9a8a7a 50%, #5a4a3c 100%); }
</style>
</head>
<body>
  <aside class="profile-sidebar">
    <div class="profile-avatar" role="img" aria-label="Profile photo of Gordon Hale"></div>
    <h1 class="profile-name">Gordon Hale</h1>
    <div class="sidebar-rule top"></div>
    <h2 class="section-label">Video Gallery</h2>
    <div class="sidebar-rule bottom"></div>
    <div class="video-thumb" role="img" aria-label="Video still of a festival crowd under a cloudy sky">
      <span class="video-title">gordon hale night valley set</span>
      <svg class="video-play" width="11" height="12" viewBox="0 0 11 12" aria-hidden="true">
        <path d="M1 1 L10 6 L1 11 Z" fill="#ffffff" opacity="0.9"/>
      </svg>
    </div>
    <nav class="sidebar-footer">
      <span>Chatterly</span>
      <span>Chirpline</span>
      <span>Linkwork</span>
    </nav>
  </aside>

  <main class="events">
    <h2 class="events-heading">Up-Comming Events</h2>
    <div class="events-rule"></div>

    <article class="event-card" style="top:128px">
      <div class="event-image img-sunset" role="img" aria-label="Silhouette holding a heart balloon at sunset"></div>
      <div class="event-text">
        <h3 class="event-title">Title of Event</h3>
        <p class="event-desc">Very short description of the event.</p>
      </div>
    </article>

    <article class="event-card" style="top:254px">
      <div class="event-image img-meadow" role="img" aria-label="Family running across a green meadow"></div>
      <div class="event-text">
        <h3 class="event-title">Title of Event</h3>
        <p class="event-desc">Very short description of the event.</p>
      </div>
    </article>

    <article class="event-card" style="top:379px">
      <div class="event-image img-balloons" role="img" aria-label="Raised arms silhouetted against coloured balloons"></div>
      <div class="event-text">
        <h3 class="event-title">Title of Event</h3>
        <p class="event-desc">Very short description of the event.</p>
      </div>
    </article>

    <article class="event-card" style="top:504px">
      <div class="event-image img-aviator" role="img" aria-label="Child in aviator goggles with arms spread wide"></div>
      <div class="event-text">
        <h3 class="event-title">Title of Event</h3>
        <p class="event-desc">Very short description of the event.</p>
      </div>
    </article>
  </main>
</body>
</html>
```